Case Management business card

Catastrophic Case Management
I'm looking for a design that best fits the words Bellwether and Catastrophic.
We need a business card for a new business based in Michigan Called Bellwether Trauma Care Coordination Group, LLC.
We provide services to clients who have been injured in a car accident and requires assistance of a case manager to facilitate and collaborate care services with or for them to help them on the road from injury to recovery. We would like to use the colors green and orange. The final design should communicate health maintenance and recovery.
We offer an comprehensive head to toe assessment.
We facilitate collaboration with your personalized injury care team members.
We assist with home and attendant care services.
We have a Team of Case managers who's main focus is continuity of care and recovery from motor vehicle injuries.

Industry/Entity Type

Business

Contact Information for Business Card

Bellwether Trauma Care Coordination Group, LLC
Catastrophic and Medical Case Management Services
2843 N. Larchmont # 538162
Harrowgate Michigan 48320
Dana Whitlow RN, CM
Director of Case Management
dwhitlow@bellwethertccg.example
Ph: 734-555-0187
Fax: 734-555-0142

```html
<!DOCTYPE html>
<html lang="en">
<head>
<meta charset="utf-8">
<title>Bellwether Trauma Care Coordination Group – Business Card</title>
<link rel="stylesheet" href="https://fonts.googleapis.com/css2?family=Gelasio:ital,wght@0,400;0,700;1,400&family=Source+Sans+3:wght@400&display=swap">
<style>
  :root {
    --green: #1f8a3c;
    --green-deep: #218f39;
    --orange: #f07d1a;
    --white: #ffffff;
    --backdrop: #f2f2f0;
  }
  * { box-sizing: border-box; margin: 0; padding: 0; }
  html, body { width: 1200px; height: 1120px; overflow: hidden; }
  body {
    background: var(--backdrop);
    font-family: "Gelasio", Georgia, serif;
    display: flex;
    align-items: center;
    justify-content: center;
    gap: 40px;
  }
  .card {
    width: 560px;
    height: 318px;
    position: relative;
    box-shadow: 0 4px 12px rgba(0,0,0,0.18);
    overflow: hidden;
  }
  .card--front {
    background: var(--white);
    color: var(--green);
    text-align: center;
    padding-top: 40px;
  }
  .wordmark {
    font-weight: 700;
    font-size: 26px;
    line-height: 1.18;
    color: var(--green);
  }
  .person { margin-top: 24px; }
  .person__name { font-size: 22px; line-height: 1.2; }
  .person__title {
    font-style: italic;
    font-size: 17px;
    color: var(--orange);
    line-height: 1.3;
  }
  .contact {
    margin-top: 24px;
    font-size: 16.5px;
    line-height: 1.38;
    font-style: normal;
  }
  .sep, .at { color: var(--orange); }
  .card--back { background: var(--green-deep); }
  .pattern {
    position: absolute; inset: 0;
    background: linear-gradient(135deg, var(--green-deep), #2a933a 50%, var(--green-deep));
  }
  .back-content {
    position: absolute; left: 0; right: 0; top: 0; bottom: 40px;
    display: flex; align-items: center; justify-content: center;
  }
  .card--back .wordmark {
    color: var(--white);
    font-size: 28px;
    text-align: center;
  }
  .tagline {
    position: absolute;
    left: 0; right: 0; bottom: 20px;
    text-align: center;
    font-family: "Source Sans 3", Arial, sans-serif;
    font-size: 14px;
    letter-spacing: 0.2px;
    color: var(--white);
  }
</style>
</head>
<body>
  <section class="card card--front" aria-label="Business card front">
    <h1 class="wordmark">Bellwether Trauma Care<br>Coordination Group, LLC</h1>
    <div class="person">
      <p class="person__name">Dana Whitlow RN, CM</p>
      <p class="person__title">Director of Case Management</p>
    </div>
    <address class="contact">
      2843 N. Larchmont # 538162 <span class="sep">|</span> Harrowgate Michigan 48320<br>
      Ph: 734-555-0187 <span class="sep">|</span> Fax: 734-555-0142<br>
      dwhitlow<span class="at">@</span>bellwethertccg.example
    </address>
  </section>

  <section class="card card--back" aria-label="Business card back">
    <div class="pattern" role="img" aria-label="Repeating green and olive wave pattern background"></div>
    <div class="back-content">
      <p class="wordmark">Bellwether Trauma Care<br>Coordination Group, LLC</p>
    </div>
    <p class="tagline">CATASTROPHIC AND MEDICAL CASE MANAGEMENT SERVICES</p>
  </section>
</body>
</html>
```